R9 Construction USA

We are General Contractors performing Federal Contracting two generations, website with one page our 'Capability Statement", five page website, want to as soon as possible secure page and Under Construction with R9 logo. No files to upload yet, time to assemble.

Coded - Design and coding required

1 page

```html
<!DOCTYPE html>
<html lang="en">
<head>
<meta charset="utf-8">
<title>R9 Construction USA</title>
<link href="https://fonts.googleapis.com/css2?family=Space+Grotesk:wght@400;500;600;700&family=Inter:wght@400;500;600;700&display=swap" rel="stylesheet">
<style>
:root{
  --navy:#0b1a3a;
  --navy-deep:#08152f;
  --navy-field:#10285a;
  --red:#c8102e;
  --ink:#0b1a3a;
  --body:#3c4556;
  --muted:#7b8394;
  --mist:#eef0f3;
  --mist-dark:#e4e7ec;
  --white:#ffffff;
}
*{margin:0;padding:0;box-sizing:border-box}
html,body{width:1200px;height:4118px;overflow:hidden;background:var(--white)}
body{font-family:"Inter",sans-serif;color:var(--body);position:relative}
section,header,footer{position:absolute;left:0;width:1200px}
.abs{position:absolute}
.eyebrow{font-family:"Inter",sans-serif;font-size:11px;font-weight:700;letter-spacing:3.5px;color:var(--red);text-transform:uppercase}

/* header */
.site-header{top:0;height:68px;background:var(--white);box-shadow:0 1px 0 #e6e8ec;z-index:5}
.brand{display:flex;align-items:center;gap:8px;left:93px;top:16px;height:36px}
.brand-dot{width:34px;height:34px;border-radius:50%;background:var(--navy)}
.brand-name{font-family:"Space Grotesk",sans-serif;font-weight:700;font-size:16px;letter-spacing:1.2px;color:var(--navy);text-transform:uppercase}
.nav{left:539px;top:26px;display:flex;gap:38px;font-size:12.5px;font-weight:500;letter-spacing:1.6px;color:var(--navy)}
.nav-cta{left:962px;top:16px;width:148px;height:36px;background:var(--navy);color:var(--white);font-size:11.5px;font-weight:700;letter-spacing:1.6px;display:flex;align-items:center;justify-content:center}

/* hero */
.hero{top:68px;height:900px;overflow:hidden}
.hero-photo{inset:0;background:linear-gradient(90deg,#14356f 0%,#284f86 30%,#5f7c9c 60%,#8ea3b6 100%)}
.hero-shade{inset:0;background:linear-gradient(180deg,rgba(11,26,58,.05) 0%,rgba(11,26,58,.35) 100%)}
.badge{left:90px;top:221px;height:19px;padding:0 10px;background:var(--red);color:var(--white);font-size:9.5px;font-weight:700;letter-spacing:1.8px;display:flex;align-items:center}
.hero-title{left:90px;top:262px;font-family:"Space Grotesk",sans-serif;font-weight:700;font-size:88px;line-height:112px;letter-spacing:-2px;color:var(--white)}
.hero-lede{left:90px;top:518px;width:560px;font-size:21.5px;line-height:30px;color:#f1f4f9}
.btn{height:58px;display:flex;align-items:center;justify-content:center;font-size:12.5px;font-weight:700;letter-spacing:1.6px;color:var(--white)}
.btn-solid{left:90px;top:622px;width:305px;background:var(--navy)}
.btn-line{left:409px;top:622px;width:167px;border:1.5px solid rgba(255,255,255,.9)}
.hero-accent{left:90px;top:781px;width:4px;height:119px;background:var(--red)}

/* legacy */
.legacy{top:968px;height:863px;background:var(--white)}
.legacy-photo{left:90px;top:150px;width:450px;height:563px;background:linear-gradient(160deg,#9a9a9a 0%,#4a4a4a 50%,#1f1f1f 100%)}
.quote-card{left:300px;top:516px;width:300px;height:226px;background:var(--navy-deep);padding:46px 44px}
.quote-card p{width:180px;font-family:"Space Grotesk",sans-serif;font-weight:500;font-size:27px;line-height:35px;color:var(--white)}
.quote-card span{display:block;margin-top:18px;font-size:10.5px;letter-spacing:2.2px;color:#8d97ab}
.legacy-eyebrow{left:660px;top:170px}
.legacy-title{left:660px;top:210px;font-family:"Space Grotesk",sans-serif;font-weight:700;font-size:57px;line-height:57px;color:var(--ink)}
.legacy-rule{left:660px;top:414px;width:90px;height:5px;background:var(--navy)}
.legacy-copy{left:660px;top:455px;width:445px;font-size:16px;line-height:27.6px;color:var(--body)}
.stat{top:632px}
.stat b{display:block;font-family:"Space Grotesk",sans-serif;font-weight:600;font-size:32px;color:var(--ink);line-height:36px}
.stat small{display:block;margin-top:14px;font-size:11px;letter-spacing:1.8px;color:var(--muted)}

/* services */
.services{top:1831px;height:985px;background:var(--mist)}
.services-edge{left:0;top:0;width:29px;height:985px;background:var(--mist-dark)}
.services-eyebrow{left:90px;top:152px}
.services-title{left:90px;top:176px;font-family:"Space Grotesk",sans-serif;font-weight:700;font-size:57px;line-height:58px;color:var(--ink)}
.services-rule{left:754px;top:291px;width:310px;height:1px;background:#cfd4dc}
.cards{left:90px;top:368px;display:flex;gap:4px}
.card{width:337px;height:495px;background:var(--white);padding:43px 45px}
.card-art{width:234px;height:160px;background:linear-gradient(135deg,#f4f4f4,#d9d9d9)}
.card h3{margin-top:44px;font-family:"Space Grotesk",sans-serif;font-weight:600;font-size:22px;line-height:29px;letter-spacing:.3px;color:var(--ink);text-transform:uppercase}
.card p{margin-top:26px;width:242px;font-size:14.5px;line-height:24.5px;color:var(--body)}
.card.tall h3{margin-top:28px}
.card.tall p{width:218px}

/* contact */
.contact{top:2816px;height:847px;background:var(--white);overflow:hidden}
.contact-slab{inset:0}
.contact-title{left:90px;top:148px;font-family:"Space Grotesk",sans-serif;font-weight:700;font-size:66px;line-height:67px;color:var(--ink)}
.contact-lede{left:90px;top:388px;width:400px;font-size:18.5px;line-height:27px;color:var(--body)}
.contact-item{left:90px;display:flex;align-items:center;gap:22px}
.icon-box{width:45px;height:45px;background:var(--mist);display:flex;align-items:center;justify-content:center}
.contact-item small{display:block;font-size:10.5px;letter-spacing:1.8px;color:var(--muted)}
.contact-item b{display:block;margin-top:6px;font-family:"Space Grotesk",sans-serif;font-weight:600;font-size:19px;color:var(--ink)}
.form{left:646px;top:150px;width:464px;height:558px;background:var(--navy-deep);padding:60px 59px}
.form label{display:block;font-size:9.5px;font-weight:700;letter-spacing:2.2px;color:#c3cad8}
.field{margin-top:9px;height:53px;background:var(--navy-field);border-bottom:2px solid #2f4c84;padding:0 11px;display:flex;align-items:center;font-size:14px;color:#6d83ad}
.field.area{height:122px;align-items:flex-start;padding-top:14px}
.form .gap{margin-top:30px}
.send{margin-top:22px;height:61px;background:var(--red);display:flex;align-items:center;justify-content:center;color:var(--white);font-size:13px;font-weight:700;letter-spacing:2px}

/* footer */
.site-footer{top:3663px;height:455px;background:var(--navy-deep)}
.foot-brand{left:90px;top:97px;display:flex;align-items:center;gap:8px}
.foot-brand .brand-dot{background:var(--white)}
.foot-brand .brand-name{color:var(--white)}
.foot-about{left:90px;top:150px;width:365px;font-size:12.5px;line-height:21.5px;color:#8a94a8}
.foot-col{top:80px}
.foot-col h4{font-size:11px;font-weight:700;letter-spacing:2.4px;color:var(--white);margin-bottom:20px}
.foot-col li{list-style:none;font-size:12.5px;color:#8a94a8;line-height:33.5px}
.foot-line{left:90px;top:316px;width:1020px;height:1px;background:#1a2849}
.foot-legal{left:90px;top:355px;font-size:10px;letter-spacing:2px;color:#6c7690}
.foot-social{right:90px;top:355px;display:flex;gap:30px;font-size:10px;letter-spacing:2px;color:#6c7690}
</style>
</head>
<body>

<header class="site-header">
  <div class="brand abs"><span class="brand-dot"></span><span class="brand-name">R9 Construction USA</span></div>
  <nav class="nav abs"><span>ABOUT</span><span>SERVICES</span><span>PROJECTS</span><span>CONTACT</span></nav>
  <div class="nav-cta abs">GET A QUOTE</div>
</header>

<section class="hero">
  <div class="hero-photo abs" role="img" aria-label="Dam and bridge construction site with tower cranes over a river at dawn"></div>
  <div class="hero-shade abs"></div>
  <div class="badge abs">ESTABLISHED 1984</div>
  <h1 class="hero-title abs">Building Excellence.<br>Federal Standards.</h1>
  <p class="hero-lede abs">Two generations of unyielding expertise in federal contracting and heavy infrastructure development.</p>
  <div class="btn btn-solid abs">VIEW CAPABILITY STATEMENT&nbsp;&nbsp;→</div>
  <div class="btn btn-line abs">CONTACT US</div>
  <div class="hero-accent abs"></div>
</section>

<section class="legacy">
  <div class="legacy-photo abs" role="img" aria-label="Black and white photo of a concrete structural frame rising against a cloudy sky"></div>
  <div class="quote-card abs">
    <p>”Trust is engineered, not given.”</p>
    <span>— THE R9 LEGACY</span>
  </div>
  <div class="eyebrow legacy-eyebrow abs">Our Legacy of Trust</div>
  <h2 class="legacy-title abs">Decades of<br>Structural<br>Integrity.</h2>
  <div class="legacy-rule abs"></div>
  <p class="legacy-copy abs">Rooted in decades of experience, we bridge the gap between complex federal requirements and high-quality infrastructure delivery. Our commitment to compliance and excellence is built into every square foot of the projects we manage.</p>
  <div class="stat abs" style="left:660px"><b>35+</b><small>YEARS OF EXPERIENCE</small></div>
  <div class="stat abs" style="left:900px"><b>500+</b><small>FEDERAL CONTRACTS</small></div>
</section>

<section class="services">
  <div class="services-edge abs"></div>
  <div class="eyebrow services-eyebrow abs">Core Competencies</div>
  <h2 class="services-title abs">Mission-Critical<br>Construction Services.</h2>
  <div class="services-rule abs"></div>
  <div class="cards abs">
    <article class="card tall">
      <div class="card-art" role="img" aria-label="Sketch of a handshake in front of a hard hat and blueprints"></div>
      <h3>General<br>Contracting</h3>
      <p>End-to-end management of sophisticated builds, ensuring every nail and beam meets architectural intent and safety codes.</p>
    </article>
    <article class="card">
      <div class="card-art" role="img" aria-label="Sketch of a capitol building with a flag"></div>
      <h3>Federal Projects</h3>
      <p>Specializing in SCIF, military housing, and high-security government installations requiring strict clearance and compliance.</p>
    </article>
    <article class="card">
      <div class="card-art" role="img" aria-label="Sketch of rebar mesh and a steel I-beam"></div>
      <h3>Infrastructure</h3>
      <p>Critical public works including bridge maintenance, highway expansion, and large-scale water treatment facility development.</p>
    </article>
  </div>
</section>

<section class="contact">
  <svg class="contact-slab abs" width="1200" height="847" viewBox="0 0 1200 847"><polygon points="1090,0 1200,0 1200,847 914,847" fill="#f1f2f4"/></svg>
  <h2 class="contact-title abs">Let’s Build<br>Something<br>That Lasts.</h2>
  <p class="contact-lede abs">Ready to discuss your next federal or large-scale infrastructure project? Our engineering team is standing by.</p>
  <div class="contact-item abs" style="top:505px">
    <div class="icon-box"><svg width="18" height="18" viewBox="0 0 24 24" fill="none" stroke="#0b1a3a" stroke-width="1.8" stroke-linejoin="round"><path d="M5 3h4l2 5-2.5 1.5a11 11 0 0 0 6 6L16 13l5 2v4a2 2 0 0 1-2 2A16 16 0 0 1 3 5a2 2 0 0 1 2-2z"/></svg></div>
    <div><small>DIRECT LINE</small><b>+1 (800) 555-0147</b></div>
  </div>
  <div class="contact-item abs" style="top:582px">
    <div class="icon-box"><svg width="18" height="18" viewBox="0 0 24 24" fill="none" stroke="#0b1a3a" stroke-width="1.8"><rect x="3" y="5" width="18" height="14" rx="1"/><path d="M3 6l9 7 9-7"/></svg></div>
    <div><small>CONTRACTING OFFICE</small><b>contracts@r9usa.com</b></div>
  </div>
  <div class="contact-item abs" style="top:659px">
    <div class="icon-box"><svg width="18" height="18" viewBox="0 0 24 24" fill="none" stroke="#0b1a3a" stroke-width="1.8"><path d="M12 22s7-6.5 7-12a7 7 0 0 0-14 0c0 5.5 7 12 7 12z"/><circle cx="12" cy="10" r="2.5"/></svg></div>
    <div><small>HEADQUARTERS</small><b>450 Meridian Avenue, Washington D.C.</b></div>
  </div>
  <form class="form abs">
    <label>FULL NAME</label>
    <div class="field">John Doe</div>
    <label class="gap">EMAIL ADDRESS</label>
    <div class="field">john@agency.gov</div>
    <label class="gap">PROJECT DETAILS</label>
    <div class="field area">Describe the scope of work...</div>
    <div class="send">SEND INQUIRY</div>
  </form>
</section>

<footer class="site-footer">
  <div class="foot-brand abs"><span class="brand-dot"></span><span class="brand-name">R9 Construction USA</span></div>
  <p class="foot-about abs">Exceeding federal requirements through generational expertise and technical precision. Licensed and bonded for major infrastructure works across 50 states.</p>
  <div class="foot-col abs" style="left:623px">
    <h4>CAPABILITIES</h4>
    <ul><li>Design-Build</li><li>Project Management</li><li>Safety Compliance</li><li>Asset Renewal</li></ul>
  </div>
  <div class="foot-col abs" style="left:888px">
    <h4>LEGAL</h4>
    <ul><li>Capability Statement</li><li>Vendor ID &amp; Codes</li><li>Privacy Policy</li><li>Terms of Use</li></ul>
  </div>
  <div class="foot-line abs"></div>
  <div class="foot-legal abs">© 2024 R9 CONSTRUCTION USA. ALL RIGHTS RESERVED.</div>
  <div class="foot-social abs"><span>NETLINK</span><span>BIDWIRE</span><span>REGISTRY HUB</span></div>
</footer>

</body>
</html>
```